New Brochures to deliver confidence of our company to our customers

I would like to have new brochure to be used to distribute to our prospective customers besides the power point presentation. I like the powerpoint you did for us and would like to follow the direction that you have set up. I will attach a number of photos for you to include in our brochure for you to choose. I like the brochure to be modern and forward thinking but just practical. The brochure needs to have three languages which are English, Chinese and Japanese. Attaches is the power point that we like.

Target Market(s)

Multinational companies

Industry/Entity Type

Electronics

Colors

Designer to choose colors to be used in the design.

Requirements
Must have
• Feel lively and modern and yet giving people a sense of confidence. Highlighting the automation is important. Can let us know if you want more photos. The brochure will have three languages, namely english, japanese and chinese.

```html
<!DOCTYPE html>
<html lang="en">
<head>
<meta charset="utf-8">
<title>KVT Brochure – Background Spread</title>
<link href="https://fonts.googleapis.com/css2?family=Oswald:wght@600&family=Open+Sans:wght@400;700&display=swap" rel="stylesheet">
<style>
  :root {
    --bg: #f2f2f2;
    --paper: #ffffff;
    --ink: #2b2b2b;
    --brand-green: #1f5a32;
    --title-ink: #163322;
    --footer-grey: #a9a9a9;
    --footer-text: #e4e4e4;
    --hero-dark: #0d3a40;
    --hero-light: #3f9aa0;
  }
  * { box-sizing: border-box; margin: 0; padding: 0; }
  html, body { width: 1200px; height: 900px; overflow: hidden; background: var(--bg); }
  body { font-family: "Open Sans", Arial, sans-serif; color: var(--ink); }

  .spread {
    position: absolute; left: 60px; top: 68px;
    width: 1080px; height: 764px;
    display: flex;
    box-shadow: 0 12px 40px rgba(0,0,0,.18);
  }
  .page { position: relative; width: 540px; height: 764px; background: var(--paper); overflow: hidden; }
  .page--left { border-right: 1px solid #e2e2e2; }

  .brand { position: absolute; top: 18px; right: 34px; text-align: right; }
  .brand__name {
    display: flex; align-items: center; justify-content: flex-end; gap: 8px;
    font-family: "Oswald", sans-serif; font-weight: 600; font-size: 30px;
    letter-spacing: 4px; color: var(--brand-green); line-height: 1;
  }
  .brand__mark { width: 14px; height: 14px; background: var(--brand-green); }
  .brand__tagline { font-size: 6.5px; font-weight: 700; letter-spacing: .6px; color: var(--ink); margin-top: 3px; }

  .hero {
    position: absolute; top: 72px; left: 0; width: 540px; height: 160px;
    background: linear-gradient(120deg, var(--hero-dark) 0%, #1d6a70 45%, var(--hero-light) 75%, #0f4a50 100%);
  }

  .title {
    position: absolute; top: 252px; left: 34px;
    font-family: "Oswald", sans-serif; font-weight: 600; font-size: 28px;
    line-height: 1.05; color: var(--title-ink);
  }

  .col { position: absolute; width: 232px; font-size: 8.6px; line-height: 1.38; text-align: justify; }
  .col p { margin-bottom: 6px; }
  .col--a { left: 34px; top: 330px; }
  .col--b { left: 284px; top: 248px; }
  .col h3 { font-size: 8.8px; font-weight: 700; color: var(--brand-green); letter-spacing: .6px; text-transform: uppercase; margin: 8px 0 4px; line-height: 1.25; text-align: left; }
  .col h4 { font-size: 9px; font-weight: 700; margin: 10px 0 3px; }

  .footer {
    position: absolute; left: 0; bottom: 0; width: 100%; height: 52px;
    background: var(--footer-grey); color: var(--footer-text);
    font-size: 16px; display: flex; align-items: center; padding: 0 34px;
  }
  .footer--right { justify-content: flex-end; }

  .gallery { position: absolute; left: 22px; top: 78px; width: 496px; height: 610px; }
  .photo { position: absolute; }
  .photo--1 { left: 0; top: 0; width: 246px; height: 150px; background: linear-gradient(135deg,#d9d6cf,#8a6a3e 55%,#c9c9c5); }
  .photo--2 { left: 252px; top: 0; width: 244px; height: 196px; background: linear-gradient(160deg,#cfd3d0,#5c8a5e 50%,#e9ebe8); }
  .photo--3 { left: 0; top: 156px; width: 200px; height: 236px; background: linear-gradient(180deg,#d8d8d6,#4a4a4c 55%,#b6b6b2); }
  .photo--4 { left: 206px; top: 202px; width: 290px; height: 190px; background: linear-gradient(140deg,#e3e6ea,#c7cfd6 45%,#e4d36a 70%,#bdbdbd); }
  .photo--5 { left: 0; top: 398px; width: 496px; height: 212px; background: linear-gradient(180deg,#e7e7e5,#b2b6b0 45%,#6d6f6c 100%); }
</style>
</head>
<body>
<main class="spread">
  <section class="page page--left">
    <div class="brand">
      <div class="brand__name"><span class="brand__mark"></span>KVT</div>
      <div class="brand__tagline">Precision Boards, Built to Last</div>
    </div>
    <div class="hero" role="img" aria-label="Close-up photo of a microchip on a teal circuit board"></div>

    <h1 class="title">KVT<br>Background</h1>

    <div class="col col--a">
      <p>Established in 2007, Korvant Circuits Limited (KVT) is a Hong Kong company specializing in single and double sided printed circuit boards. Its manufacturing facility is located in a self-owned facility in southern China which is 50 minutes from Hong Kong.</p>
      <p>Our mission is to become a premium low costs PCB supplier that fully embraces human, social and environmental responsibilities.</p>
      <p>Through our insatiable drive to maximize efficiency, KVT is becoming a highly efficient PCB factory with a capacity of 140,000 sq meter a month.</p>
      <p>PCB is our business and it is through continued automation and innovation that will drive our growth in the next 10 years.</p>
      <h3>Single layered printed circuit boards</h3>
      <p>We are offering single layered circuit boards through our own production facility in China for customers in the following industries:</p>
    </div>

    <div class="col col--b">
      <h3>Double layered and multi-layered printed circuit boards</h3>
      <p>We are offering two layered and multi-layered circuit boards for our customers through our strategically approved printed circuit boards manufacturers.</p>
      <p>With our own UL for double sided and multi-layered circuit boards, we work with a number of strategically approved manufacturers in delivering 100% quality guaranteed printed circuit boards for our customers.</p>
      <p>All the PCBs are inspected by our own Automatic Visual Inspection (AVI) Machine before we deliver to customers.</p>
      <p>We perform comprehensive quality and environmental audit of our manufacturers on quarterly and annual basis.</p>
      <h4>Our investment and upgrade</h4>
      <p>Maintaining a highly automated factory is the only way to ensure consistent product and long term competitive efficiency.</p>
      <p>From 2015 to 2017, KVT invested over US$3.5 million in automating our production and quality control process and enhancing our environmental processing facility. We will spend a further US$1.5 million in 2018 to continue our improvement process to ensure we are one of the most efficient and highest quality single sided PCB manufacturers in Asia. By the end of 2018, 100% of our PCBs will be inspected by AVI before they are delivered to our customers.</p>
    </div>

    <footer class="footer">02</footer>
  </section>

  <section class="page page--right">
    <div class="brand">
      <div class="brand__name"><span class="brand__mark"></span>KVT</div>
      <div class="brand__tagline">Precision Boards, Built to Last</div>
    </div>
    <div class="gallery">
      <div class="photo photo--1" role="img" aria-label="Automated reflow machine with viewing window"></div>
      <div class="photo photo--2" role="img" aria-label="Green conveyor line on the factory floor"></div>
      <div class="photo photo--3" role="img" aria-label="Plating line with tanks and hoists"></div>
      <div class="photo photo--4" role="img" aria-label="Roller conveyor carrying a circuit board panel"></div>
      <div class="photo photo--5" role="img" aria-label="Hall of automated drilling machines"></div>
    </div>
    <footer class="footer footer--right">03</footer>
  </section>
</main>
</body>
</html>
```